Sale of South Sea and Tahitian Pearl Jewellery, online business

I need a business card designed for my website business. We sell South Sea and Tahitian Pearl Jewellery. The colour theme for the website is black and white and would like to carry this through to business cards. Our brand is very elegant and stylish, would like sketch picture of women or fashion involving pearls if not the sketched picture then have the card very plan. below are pictures of the ideas I like and also the logo and writing that is used on my jewellery boxes.
Font is English Hand DB

Target Market(s)

30 and over women in the high end of the market

Industry/Entity Type

Business

Contact Information for Business Card

Business name - Varno Gems( front of card)
Back of card -Details
Rosalind Thackery
Gemmologist MDRS
email: rosalind@varnogems.com.au
website: varnogems.com.au
mob: +61 427 508 193
Ardley Westmark

Varno Stelle PTY T/AS Varno Gems
ABN 47 283 915 604

Colors
1b1b1b
ffffff
85cae6

Requirements
Must have
• Black and white colour preferably black card with white writing and picture.
• The Same writing as logo and writing on box packaging, attached a file with writing.
• Business name on one side of the card and all other details on the other side.
• Can have tiny hints of the harbour blue colour.
• Font: English Hand DB
Nice to have
• I really like the idea of having a sketch of a stylish or elegent lady wearing pearls or a sketch of a pearl, if not the sketch a really plain and simple card.
Should not have
• busy patterns.

```html
<!DOCTYPE html>
<html lang="en">
<head>
<meta charset="utf-8">
<title>Varno Gems — Business Card</title>
<link rel="stylesheet" href="https://fonts.googleapis.com/css2?family=Pinyon+Script&family=Arimo:wght@400;700&display=swap">
<style>
  :root {
    --stage-edge: #3a3a3a;
    --stage-mid: #5c5c5c;
    --card-white: #ffffff;
    --card-black: #000000;
    --ink: #1b1b1b;
    --ink-soft: #2a2a2a;
    --paper: #ffffff;
    --harbour-blue: #85cae6;
    --sketch-light: #f2f2f2;
    --sketch-dark: #9a9a9a;
  }
  * { box-sizing: border-box; margin: 0; padding: 0; }
  html, body {
    width: 999px;
    height: 1200px;
    overflow: hidden;
  }
  body {
    position: relative;
    background: radial-gradient(ellipse at center, var(--stage-mid) 0%, var(--stage-edge) 100%);
    font-family: "Arimo", Arial, sans-serif;
  }
  .card {
    position: absolute;
    left: 44px;
    width: 910px;
    height: 519px;
  }
  .card--front { top: 66px; background: var(--card-white); color: var(--ink); }
  .card--back { top: 621px; background: var(--card-black); }

  .script {
    font-family: "Pinyon Script", cursive;
    font-weight: 400;
    line-height: 1;
    position: absolute;
    white-space: nowrap;
  }
  .business-name { left: 30px; top: 76px; font-size: 100px; color: var(--ink); }
  .holder-name { left: 34px; top: 279px; font-size: 56px; color: var(--ink); }
  .holder-title {
    position: absolute; left: 32px; top: 342px;
    font-size: 22px; line-height: 1; color: var(--ink-soft);
  }

  .lady-sketch {
    position: absolute; left: 608px; top: 14px;
    width: 294px; height: 330px;
    background: radial-gradient(ellipse at 55% 40%, var(--sketch-light) 0%, var(--sketch-dark) 100%);
    border-radius: 4px;
  }

  .contact-list {
    position: absolute; left: 32px; top: 407px;
    list-style: none;
  }
  .contact-list li {
    display: flex; align-items: center;
    height: 30px;
    font-size: 23px; color: var(--ink-soft);
  }
  .contact-list svg { width: 16px; height: 16px; margin-right: 23px; flex: none; }

  .company-details {
    position: absolute; left: 517px; top: 407px;
    font-size: 23px; color: var(--ink-soft);
  }
  .company-details p { height: 30px; line-height: 30px; }
  .company-details strong { font-weight: 700; color: var(--ink); }

  .back-seal {
    position: absolute; left: 303px; top: 107px;
    width: 306px; height: 306px;
    border: 4px solid var(--paper);
    border-radius: 50%;
    display: flex; align-items: center; justify-content: center;
  }
  .back-seal .brand-name {
    position: static;
    font-size: 48px;
    color: var(--paper);
  }
</style>
</head>
<body>
  <section class="card card--front" aria-label="Business card front">
    <h1 class="script business-name">Varno Gems</h1>

    <div class="lady-sketch" role="img" aria-label="Black line sketch of an elegant woman in profile with floral ornamented hair, wearing a pearl pendant"></div>

    <h2 class="script holder-name">Rosalind Thackery</h2>
    <p class="holder-title">Gemmologist MDRS</p>

    <ul class="contact-list">
      <li>
        <svg viewBox="0 0 16 16" aria-hidden="true"><rect x="3" y="1" width="10" height="14" rx="2" fill="var(--ink)"/><rect x="5" y="3" width="6" height="9" fill="var(--paper)"/></svg>
        +61 427 508 193
      </li>
      <li>
        <svg viewBox="0 0 16 16" aria-hidden="true"><path d="M1 6 L8 1 L15 6 V15 H1 Z" fill="var(--ink)"/><path d="M1 6 L8 11 L15 6" fill="none" stroke="var(--paper)" stroke-width="1.3"/></svg>
        rosalind@varnogems.com.au
      </li>
      <li>
        <svg viewBox="0 0 16 16" aria-hidden="true"><g fill="none" stroke="var(--ink)" stroke-width="1.2"><circle cx="8" cy="8" r="7"/><ellipse cx="8" cy="8" rx="3" ry="7"/><path d="M1 8 H15 M2.5 4.5 H13.5 M2.5 11.5 H13.5"/></g></svg>
        varnogems.com.au
      </li>
    </ul>

    <div class="company-details">
      <p><strong>Ardley Westmark</strong></p>
      <p>Varno Stelle PTY T/AS Varno Gems</p>
      <p><strong>ABN</strong> 47 283 915 604</p>
    </div>
  </section>

  <section class="card card--back" aria-label="Business card back">
    <div class="back-seal">
      <span class="script brand-name">Varno Gems</span>
    </div>
  </section>
</body>
</html>
```